Fertility consulting business needs oversized postcard handout

We need an oversized postcard that we can hand out and leave around in many places. It needs to be an overview of our business and get people to go to the website to sign up for a class.

I am including exact verbiage in "Must Haves" section.
Colors used should be colors from logo. And website: www.lunabloomcycles.com Or, a brown base, with colors from logo. Will send a scan of business card that is set up this way.
Two-sided.
Will print with Prentora

Target Market(s)

women

Industry/Entity Type

Business

Font styles to use
Sans Serif
Script

Requirements
Must have
• FRONT:
• logo
• The TRUTH every woman deserves to know about her fertility.
• The Halvery Method is a system of fertility awareness education. Women and couples can fully understand their own fertility to avoid or achieve pregnancy or monitor reproductive health.
• In San Diego County and online instruction available
• Contact us at: www.lunabloomcycles.com | 619.482.5173 | www.friendloop.com/lunabloomcycles
• ON BACK:
• Learning the Halvery Method provides access to real women's healthcare and help for: [I WILL PROVIDE A LIST]
• - help for breastfeeding and coming off of hormonal birth control
• - daily observation of biomarkers and charting
• - one-on-one confidential instruction
• - 100% natural, 99.6% effective to avoid pregnancy, 75% effective to achieve pregnancy in one cycle
Nice to have
• Incorporate the photo that I will send - showing me working with a client.
Should not have
• Pictures of men.

```html
<!DOCTYPE html>
<html lang="en">
<head>
<meta charset="utf-8">
<title>Luna Bloom Cycles – Postcard Back</title>
<link rel="stylesheet" href="https://fonts.googleapis.com/css2?family=Fira+Sans+Extra+Condensed:wght@600&family=Roboto:wght@400&family=Lato:wght@700;900&family=Montserrat:wght@600&family=Open+Sans:wght@400;700&display=swap">
<style>
  :root {
    --pink: #e56a93;
    --olive: #c2c053;
    --panel: #f8f9f9;
    --white: #ffffff;
    --ink: #333333;
    --body: #444444;
    --rule: #7a7a7a;
    --black: #111111;
  }
  * { box-sizing: border-box; margin: 0; padding: 0; }
  html, body { width: 1200px; height: 776px; overflow: hidden; background: var(--white); }
  .postcard { position: relative; width: 1200px; height: 776px; overflow: hidden; background: var(--white); }

  .message-side { position: absolute; left: 0; top: 0; width: 573px; height: 742px; background: var(--panel); }
  .headline {
    position: absolute; left: 54px; top: 56px; width: 510px;
    font-family: "Fira Sans Extra Condensed", sans-serif; font-weight: 600;
    font-size: 30px; line-height: 42px; color: var(--pink); text-transform: uppercase;
  }
  .benefits { position: absolute; left: 72px; top: 210px; width: 480px; list-style: none; }
  .benefits li {
    position: relative; padding-left: 38px;
    font-family: "Roboto", sans-serif; font-size: 16.6px; line-height: 27px; color: var(--body);
  }
  .benefits li:nth-child(1) { margin-bottom: 9px; }
  .benefits li:nth-child(2) { margin-bottom: 14px; }
  .benefits .tick { position: absolute; left: 0; top: 0; width: 24px; height: 24px; }

  .contact-title { position: absolute; left: 73px; top: 508px; font-family: "Lato", sans-serif; color: var(--pink); }
  .contact-title .small { display: block; font-weight: 700; font-size: 15px; line-height: 16px; }
  .contact-title .large { display: block; font-weight: 900; font-size: 28px; line-height: 32px; text-decoration: underline; text-decoration-thickness: 3px; text-underline-offset: 3px; }

  .contact-list { position: absolute; left: 72px; top: 578px; list-style: none; }
  .contact-list li {
    position: relative; height: 44px; padding-left: 52px;
    font-family: "Montserrat", sans-serif; font-weight: 600; font-size: 17px; line-height: 32px; color: var(--ink);
  }
  .contact-list .icon { position: absolute; left: 0; top: 3px; width: 26px; height: 26px; }

  .address-side { position: absolute; left: 573px; top: 0; width: 627px; height: 742px; background: var(--white); }
  .brand { position: absolute; left: 40px; top: 40px; width: 170px; text-align: center; }
  .brand-dot { display: block; width: 44px; height: 44px; margin: 0 auto 12px; border-radius: 50%; background: var(--olive); }
  .brand-name {
    font-family: "Fira Sans Extra Condensed", sans-serif; font-weight: 600;
    font-size: 30px; line-height: 32px; color: var(--pink);
  }

  .indicia {
    position: absolute; left: 452px; top: 28px; width: 143px; height: 142px;
    border: 2px solid var(--black); padding-top: 12px; text-align: center;
    font-family: "Open Sans", sans-serif; font-size: 16px; line-height: 19.5px; color: var(--black);
  }
  .indicia strong { font-weight: 700; }

  .address-lines { position: absolute; left: 49px; top: 338px; width: 518px; }
  .address-lines span { display: block; height: 1px; background: var(--rule); margin-bottom: 102px; }

  .band { position: absolute; top: 742px; height: 34px; }
  .band-olive { left: 0; width: 573px; background: var(--olive); }
  .band-pink { left: 573px; width: 627px; background: var(--pink); }
</style>
</head>
<body>
<div class="postcard">
  <section class="message-side">
    <h1 class="headline">Learning the Halvery Method provides access to real women's healthcare and help for:</h1>

    <ul class="benefits">
      <li><svg class="tick" viewBox="0 0 24 24"><circle cx="12" cy="12" r="10" fill="none" stroke="#e56a93" stroke-width="2.4"/><path d="M7.5 12.3l3 3 6-6" fill="none" stroke="#e56a93" stroke-width="2.4" stroke-linecap="round" stroke-linejoin="round"/></svg>Lorem Ipsum is simply ummy text of mmy text of etting indupends.</li>
      <li><svg class="tick" viewBox="0 0 24 24"><circle cx="12" cy="12" r="10" fill="none" stroke="#e56a93" stroke-width="2.4"/><path d="M7.5 12.3l3 3 6-6" fill="none" stroke="#e56a93" stroke-width="2.4" stroke-linecap="round" stroke-linejoin="round"/></svg>Lorem Ipsum is simply ummy text of mmy text of etting indupends.</li>
      <li><svg class="tick" viewBox="0 0 24 24"><circle cx="12" cy="12" r="10" fill="none" stroke="#e56a93" stroke-width="2.4"/><path d="M7.5 12.3l3 3 6-6" fill="none" stroke="#e56a93" stroke-width="2.4" stroke-linecap="round" stroke-linejoin="round"/></svg>Lorem Ipsum is simply ummy text of mmy text of etting indupends.</li>
    </ul>

    <h2 class="contact-title"><span class="small">GET IN</span><span class="large">TOUCH</span></h2>

    <ul class="contact-list">
      <li><svg class="icon" viewBox="0 0 26 26"><path d="M3 9c0-3 4-5 10-5s10 2 10 5v2h-5V8.5c-1.5-.6-3-.9-5-.9s-3.5.3-5 .9V11H3z" fill="#e56a93"/><path d="M7 12h12l2 10H5z" fill="#e56a93"/><circle cx="13" cy="17" r="2.4" fill="#f8f9f9"/></svg>619.482.5173</li>
      <li><svg class="icon" viewBox="0 0 26 26"><circle cx="13" cy="13" r="11.5" fill="#e56a93"/><g fill="none" stroke="#f8f9f9" stroke-width="1.4"><ellipse cx="13" cy="13" rx="5" ry="11.5"/><line x1="13" y1="1.5" x2="13" y2="24.5"/><line x1="1.5" y1="13" x2="24.5" y2="13"/><path d="M3.5 7.5h19M3.5 18.5h19"/></g></svg>www.lunabloomcycles.com</li>
      <li><svg class="icon" viewBox="0 0 26 26"><circle cx="13" cy="13" r="6" fill="#e56a93"/></svg>www.friendloop.com/lunabloomcycles</li>
    </ul>
  </section>

  <section class="address-side">
    <div class="brand">
      <span class="brand-dot"></span>
      <p class="brand-name">Luna Bloom Cycles</p>
    </div>

    <div class="indicia">PRESORTED<br>STANDARD<br>US POSTAGE<br><strong>PAID</strong><br>ELMVALE, OH<br>PERMIT #2741</div>

    <div class="address-lines"><span></span><span></span><span></span><span></span></div>
  </section>

  <div class="band band-olive"></div>
  <div class="band band-pink"></div>
</div>
</body>
</html>
```